Logo and website for new private wealth management business

This project is for a new company website and logo. The name of the firm is Harborline Estate Partners, LLC. We are a wealth management firm offering customized financial planning and investment management services to high net worth and ultra high net worth individuals and families. I want the website to feel contemporary but convey a feeling of sophistication and prestige.
www.tolvanridgeholdings.example and www.qnfunds.example are both good reference websites.
My clients will consist of wealthy individuals and families. I have existing clients in their 50s - 70s, but I also intend to target younger business owners and entrepreneurs in their 30s -50s.

Target Market(s)

Business owners, entrepreneurs and corporate executives. Many existing clients are in their 60s and 70s, but intend to also attract a younger clientele in their 30s - 50s.

Industry/Entity Type

Wealth management, investment advisory, financial planning

Coding

Coded - Design and coding required

Colors
0054AA
0677BA
7BADD7
CADEEF
E8F1F8
0094D4
00A9DD
6FCCEA
C7EBF8
E9F6FB
00AB8E
00BBA5
67D7C9
C6EFE9
E9F9F6
EE7325
F08F49
F5BC92
FAE3D3
FDF4ED

Requirements
Must have
• Should use blue as the main color theme. Should have an About, Services, Our Clients, FAQ, and Contact sections
Should not have
• Should not have pictures of people as the background.

```html
<!DOCTYPE html>
<html lang="en">
<head>
<meta charset="utf-8">
<title>Harborline Estate Partners, LLC</title>
<link href="https://fonts.googleapis.com/css2?family=Poppins:ital,wght@0,400;0,500;0,600;0,700;1,400&display=swap" rel="stylesheet">
<style>
:root{
  --navy:#2b3565;
  --ink:#1f2a4a;
  --text:#555d6e;
  --blue:#1e9be9;
  --brand:#0677BA;
  --deep:#0a5ea9;
  --deep2:#08559a;
  --pale:#E8F1F8;
  --pale2:#f1f7fc;
  --line:#CADEEF;
  --white:#ffffff;
}
*{margin:0;padding:0;box-sizing:border-box}
html,body{width:1200px;height:5085px;overflow:hidden}
body{position:relative;font-family:'Poppins',sans-serif;color:var(--text);background:var(--white)}
.abs{position:absolute}
.btn{position:absolute;background:var(--blue);color:var(--white);font-size:14px;display:flex;align-items:center;justify-content:center;border-radius:2px}
.logo{position:absolute;display:flex;align-items:center;gap:10px;font-weight:600}
.logo .mark{width:34px;height:34px}
/* hero */
.hero-photo{left:0;top:0;width:1200px;height:690px;background:linear-gradient(160deg,#2f5a3b 0%,#4d7a4f 35%,#6e8f6a 60%,#3c4a3d 100%)}
.hero-shade{left:0;top:0;width:1200px;height:690px;background:linear-gradient(180deg,rgba(0,0,0,.25),rgba(0,0,0,.05) 50%,rgba(0,0,0,.2))}
.nav{left:420px;top:51px;display:flex;gap:26px;font-size:14px;color:var(--white)}
.hero-title{left:240px;top:220px;width:720px;text-align:center;color:var(--white);font-size:34px;font-weight:600;line-height:45px}
/* about */
.about-frame{left:172px;top:774px;width:856px;height:371px;border:5px solid var(--blue)}
.about-gap{left:166px;top:912px;width:14px;height:140px;background:var(--white)}
.about-title{left:202px;top:866px;font-size:33px;font-weight:700;line-height:52px;color:var(--ink);letter-spacing:.5px}
.about-title span{color:var(--brand)}
.about-text{left:549px;top:822px;width:438px;font-size:13px;line-height:20.6px}
/* why */
.why{left:0;top:1222px;width:1200px;height:501px;background:var(--pale2)}
.section-title{position:absolute;left:0;width:1200px;text-align:center;font-size:31px;font-weight:600;color:var(--navy)}
.feature{position:absolute;width:260px;height:81px;background:var(--white);border:1px solid #dbe6ef;border-radius:6px;box-shadow:0 3px 8px rgba(30,80,140,.08);padding:12px 16px;font-size:10.5px;line-height:15px}
.feature h4{font-size:13px;font-weight:600;color:var(--ink);margin-bottom:2px}
.feature.l{text-align:right;padding-right:70px}
.feature.r{padding-left:70px}
.feature svg{position:absolute;top:18px}
.feature.l svg{right:14px}.feature.r svg{left:14px}
.hub{left:490px;top:1394px;width:223px;height:203px;border:3px solid var(--blue);border-radius:10px;background:var(--white);padding:8px}
.hub-inner{width:100%;height:100%;border:1px solid var(--line);border-radius:6px;display:flex;align-items:center;justify-content:center}
/* services */
.photo{position:absolute;border-radius:10px}
.photo-back{position:absolute;background:#c7e3f8;border-radius:12px}
.svc-title{font-size:26px;font-weight:600;color:var(--ink)}
.svc-text{width:390px;font-size:12.5px;line-height:20.6px}
/* testimonial */
.testi{left:0;top:2920px;width:1200px;height:564px;background:var(--deep)}
.step{position:absolute;background:var(--deep2)}
.quote{left:570px;top:3180px;width:445px;font-size:14px;font-style:italic;line-height:22px;color:#d7e8f7}
/* faq */
.faq{position:absolute;width:420px;background:var(--white);border:2px solid #e6eef5;border-radius:4px;font-size:13px;color:#3c4458}
.faq .q{display:flex;align-items:center;gap:18px;height:56px;padding:0 12px}
.faq .ico{width:36px;height:36px;background:var(--pale);border-radius:3px;display:flex;align-items:center;justify-content:center;color:var(--blue);font-size:22px;line-height:1}
.faq .a{padding:0 24px 14px 12px;font-size:11px;line-height:16px;color:#777}
/* contact */
.contact-bg{left:0;top:4021px;width:1200px;height:1003px;background:linear-gradient(180deg,#f2f5f8 0%,#f6f8fa 50%,#e9eef3 85%,#dfe6ec 100%)}
.form-label{position:absolute;font-size:10.5px;color:var(--brand)}
.field{position:absolute;border:1px solid #b7c6d5;background:var(--white);font-size:11px;color:#555;padding:0 16px;display:flex;align-items:center}
/* footer */
.foot-head{font-size:16px;font-weight:500;color:var(--brand)}
.foot-link{position:absolute;left:572px;font-size:13px;color:#2a2f3d}
.ci{position:absolute;left:796px;display:flex;align-items:center;gap:20px;font-size:13px;color:#2a2f3d;line-height:20px}
.ci .dot{width:34px;height:34px;border-radius:50%;background:var(--blue);display:flex;align-items:center;justify-content:center;flex:none}
.social{position:absolute;top:4907px;width:32px;height:32px;border-radius:50%;background:var(--blue)}
.copy{left:0;top:5024px;width:1200px;height:61px;background:#c9e1f3;font-size:13px;color:#59616e;display:flex;align-items:center;justify-content:center}
.copy span{color:var(--brand);font-weight:500;margin:0 4px}
</style>
</head>
<body>

<!-- HERO -->
<div class="abs hero-photo" role="img" aria-label="Coins stacked in soil with young plants and a rising growth line over a green background"></div>
<div class="abs hero-shade"></div>
<svg class="abs" style="left:0;top:600px" width="1200" height="95" viewBox="0 0 1200 95">
  <path d="M0 30 Q300 60 600 92 Q900 60 1200 30 L1200 95 L0 95Z" fill="#fff"/>
  <path d="M0 30 Q300 60 600 92 Q900 60 1200 30 L1200 4 Q900 40 600 72 Q300 40 0 4Z" fill="#1e9be9"/>
</svg>
<div class="logo" style="left:174px;top:34px;color:#fff;font-size:12px;line-height:14px">
  <div class="mark" style="background:#fff"></div><div>Harborline Estate<br>Partners, LLC</div>
</div>
<nav class="abs nav"><span>Home</span><span>About</span><span>Services</span><span>Our Clients</span><span>FAQ</span><span>Contact</span></nav>
<div class="btn" style="left:906px;top:43px;width:120px;height:34px">Login</div>
<h1 class="abs hero-title">Financial planning and investment management services to high net worth and ultra high net worth individuals and families.</h1>
<div class="btn" style="left:509px;top:430px;width:209px;height:42px">Get Started</div>

<!-- ABOUT -->
<section>
<div class="abs about-frame"></div>
<div class="abs about-gap"></div>
<h2 class="abs about-title">ABOUT <span>HARBORLINE</span><br><span>ESTATE</span><br><span>PARTNERS LLC</span></h2>
<p class="abs about-text">Lorem ipsum dolor sit amet, consectetur adipiscing elit, sed do eiusmod tempor incididunt ut labore et dolore magna aliqua. Ut enim ad minim veniam, quis nostrud exercitation ullamco laboris nisi ut aliquip ex ea commodo consequat. Duis aute irure dolor in reprehenderit in voluptate velit esse cillum dolore eu fugiat nulla pariatur.<br>Sed ut perspiciatis unde omnis iste natus error sit voluptatem accusantium doloremque laudantium, totam rem aperiam, eaque ipsa quae ab illo inventore veritatis et quasi architecto beatae vitae dicta sunt explicabo. Nemo enim ipsam</p>
<div class="btn" style="left:549px;top:1054px;width:209px;height:42px">Learn More</div>
</section>

<!-- WHY -->
<section>
<div class="abs why"></div>
<div class="abs" style="left:0;top:1354px;width:100px;height:369px;background:#e4edf5"></div>
<div class="abs" style="left:100px;top:1440px;width:260px;height:283px;background:#eaf1f7"></div>
<div class="abs" style="left:1100px;top:1354px;width:100px;height:369px;background:#e4edf5"></div>
<div class="abs" style="left:850px;top:1460px;width:250px;height:263px;background:#eaf1f7"></div>
<h2 class="section-title" style="top:1276px">WHY WORK WITH US</h2>
<svg class="abs" style="left:0;top:0" width="1200" height="1723">
  <g fill="none" stroke="#1e9be9" stroke-width="3" stroke-dasharray="14 5">
    <path d="M432 1395 H458 V1598 H432 M458 1495 H490"/>
    <path d="M766 1395 H740 V1598 H766 M740 1495 H713"/>
  </g>
</svg>
<div class="feature l" style="left:172px;top:1354px"><h4>You Come First</h4>Lorem ipsum dolor sit amet, consectetur adipiscing elit, sed
<svg width="40" height="40" viewBox="0 0 40 40"><circle cx="20" cy="20" r="17" fill="none" stroke="#1e9be9" stroke-width="1.5"/><path d="M20 10 V30 M13 17 L20 10 L27 17" fill="none" stroke="#1e9be9" stroke-width="1.5"/></svg></div>
<div class="feature l" style="left:172px;top:1557px"><h4>Transparent Fees</h4>Lorem ipsum dolor sit amet, consectetur adipiscing elit, sed
<svg width="40" height="40" viewBox="0 0 40 40"><circle cx="20" cy="20" r="17" fill="none" stroke="#1e9be9" stroke-width="1.5"/><path d="M12 12 L28 28 M28 12 L12 28" stroke="#1e9be9" stroke-width="1.5"/></svg></div>
<div class="feature r" style="left:766px;top:1354px"><h4>Personalized Services</h4>Lorem ipsum dolor sit amet, consectetur adipiscing elit, sed
<svg width="40" height="40" viewBox="0 0 40 40"><circle cx="20" cy="20" r="17" fill="none" stroke="#1e9be9" stroke-width="1.5"/><circle cx="20" cy="20" r="9" fill="none" stroke="#1e9be9" stroke-width="1.5"/></svg></div>
<div class="feature r" style="left:766px;top:1557px"><h4>We Give Back</h4>Lorem ipsum dolor sit amet, consectetur adipiscing elit, sed
<svg width="40" height="40" viewBox="0 0 40 40"><rect x="6" y="8" width="20" height="14" fill="none" stroke="#1e9be9" stroke-width="1.5"/><path d="M4 28 H24 L34 20" fill="none" stroke="#1e9be9" stroke-width="1.5"/></svg></div>
<div class="abs hub"><div class="hub-inner">
  <div class="logo" style="position:static;color:#0677BA;font-size:13px;line-height:16px"><div class="mark" style="background:#0677BA"></div><div>Harborline Estate<br>Partners, LLC</div></div>
</div></div>
</section>

<!-- SERVICES -->
<section>
<h2 class="section-title" style="top:1802px">OUR SERVICES</h2>
<div class="photo-back" style="left:160px;top:1932px;width:378px;height:402px"></div>
<div class="photo" role="img" aria-label="Advisors reviewing financial documents with a client at a table" style="left:174px;top:1911px;width:406px;height:406px;background:linear-gradient(135deg,#c9b7a4,#8c9cb5 55%,#3d4f78)"></div>
<h3 class="abs svc-title" style="left:631px;top:1938px">Financial Planning</h3>
<p class="abs svc-text" style="left:631px;top:2001px">Sed ut perspiciatis unde omnis iste natus error sit voluptatem accusantium doloremque laudantium, totam rem aperiam, eaque ipsa quae ab illo inventore veritatis et quasi architecto beatae vitae dicta sunt explicabo. Nemo enim ipsam voluptatem quia voluptas sit aspernatur aut odit aut fugit, sed quia consequuntur magni dolores eos qui ratione voluptatem sequi nesciunt.<br>Neque porro quisquam est, qui dolorem ipsum quia dolor sit amet, consectetur, adipisci velit, sed quia non numquam eius modi tempora incidunt ut labore et dolore magnam aliquam quaerat voluptatem.</p>
<div class="btn" style="left:632px;top:2266px;width:209px;height:42px">Learn More</div>

<h3 class="abs svc-title" style="left:176px;top:2426px">Investment Management</h3>
<p class="abs svc-text" style="left:176px;top:2489px">Sed ut perspiciatis unde omnis iste natus error sit voluptatem accusantium doloremque laudantium, totam rem aperiam, eaque ipsa quae ab illo inventore veritatis et quasi architecto beatae vitae dicta sunt explicabo. Nemo enim ipsam voluptatem quia voluptas sit aspernatur aut odit aut fugit, sed quia consequuntur magni dolores eos qui ratione voluptatem sequi nesciunt.<br>Neque porro quisquam est, qui dolorem ipsum quia dolor sit amet, consectetur, adipisci velit, sed quia non numquam eius modi tempora incidunt ut labore et dolore magnam aliquam quaerat voluptatem.</p>
<div class="btn" style="left:176px;top:2752px;width:209px;height:42px">Learn More</div>
<div class="photo-back" style="left:662px;top:2420px;width:378px;height:402px"></div>
<div class="photo" role="img" aria-label="Executives in a modern office with market data screens" style="left:620px;top:2398px;width:406px;height:406px;background:linear-gradient(135deg,#9fb3c4,#4d6f8c 50%,#1f3550)"></div>
</section>

<!-- TESTIMONIALS -->
<section>
<div class="abs testi"></div>
<div class="step" style="left:0;top:3115px;width:140px;height:369px"></div>
<div class="step" style="left:140px;top:3260px;width:220px;height:224px"></div>
<div class="step" style="left:840px;top:3200px;width:270px;height:284px"></div>
<div class="step" style="left:1110px;top:3115px;width:90px;height:369px"></div>
<h2 class="section-title" style="top:2996px;color:#fff">WHAT OUR CLIENTS HAVE TO SAY</h2>
<svg class="abs" style="left:160px;top:3060px" width="380" height="380">
  <circle cx="185" cy="187" r="158" fill="none" stroke="#fff" stroke-width="1.5" stroke-dasharray="3 4"/>
  <circle cx="185" cy="187" r="130" fill="#1e9be9"/>
</svg>
<div class="abs" role="img" aria-label="Portrait of a client in a suit" style="left:223px;top:3125px;width:244px;height:244px;border-radius:50%;background:linear-gradient(180deg,#e9eef3,#b9c6d3 60%,#2c4d86)"></div>
<div class="abs" role="img" aria-label="Client portrait" style="left:375px;top:3063px;width:60px;height:60px;border-radius:50%;border:3px solid #1e9be9;background:#c8d3de"></div>
<div class="abs" role="img" aria-label="Client portrait" style="left:181px;top:3172px;width:44px;height:44px;border-radius:50%;border:3px solid #1e9be9;background:#c8d3de"></div>
<div class="abs" role="img" aria-label="Client portrait" style="left:473px;top:3261px;width:44px;height:44px;border-radius:50%;border:3px solid #1e9be9;background:#c8d3de"></div>
<div class="abs" role="img" aria-label="Client portrait" style="left:260px;top:3365px;width:60px;height:60px;border-radius:50%;border:3px solid #1e9be9;background:#c8d3de"></div>
<svg class="abs" style="left:572px;top:3122px" width="38" height="38" viewBox="0 0 38 38"><circle cx="19" cy="19" r="18" fill="#1e9be9"/><path d="M11 14h7v7l-4 7h-3l3-7h-3z M21 14h7v7l-4 7h-3l3-7h-3z" fill="#fff"/></svg>
<p class="abs quote">"Sed Ut Perspiciatis Unde Omnis Iste Natus Error Sit Voluptatem Accusantium Doloremque Laudantium, Totam Rem Aperiam, Eaque Ipsa Quae Ab Illo Inventore Veritatis Et Quasi Architecto Beatae Vitae Dicta Sunt Explicabo. Nemo Enim Ipsam Voluptatem"</p>
<div class="abs" style="left:570px;top:3300px;font-size:20px;font-weight:500;color:#fff">Rowan Ellsworth</div>
<svg class="abs" style="left:570px;top:3346px" width="100" height="20"><g fill="none" stroke="#6FCCEA" stroke-width="2"><path d="M2 10H24M9 4L2 10L9 16"/><path d="M70 10H92M85 4L92 10L85 16"/></g></svg>
</section>

<!-- FAQ -->
<section>
<h2 class="section-title" style="top:3565px">FAQ</h2>
<div class="faq" style="left:172px;top:3638px"><div class="q"><div class="ico">−</div>Lorem ipsum dolor sit amet, consectetur</div><div class="a">minim veniam, quis nostrud exercitation ullamco laboris nisi utaliquip ex ea commodo consequat. Duis aute irure dolor in nderit in voluptate velit esse cillum dolore eu</div></div>
<div class="faq" style="left:606px;top:3638px"><div class="q"><div class="ico">+</div>Lorem ipsum dolor sit amet, consectetur</div></div>
<div class="faq" style="left:606px;top:3714px"><div class="q"><div class="ico">+</div>Lorem ipsum dolor sit amet, consectetur</div></div>
<div class="faq" style="left:172px;top:3791px"><div class="q"><div class="ico">+</div>Lorem ipsum dolor sit amet, consectetur</div></div>
<div class="faq" style="left:606px;top:3791px"><div class="q"><div class="ico">+</div>Lorem ipsum dolor sit amet, consectetur</div></div>
<div class="faq" style="left:172px;top:3867px"><div class="q"><div class="ico">+</div>Lorem ipsum dolor sit amet, consectetur</div></div>
<div class="faq" style="left:606px;top:3867px"><div class="q"><div class="ico">+</div>Lorem ipsum dolor sit amet, consectetur</div></div>
</section>

<!-- CONTACT -->
<section>
<div class="abs contact-bg" role="img" aria-label="Soft misty mountain landscape in pale grey-blue"></div>
<h2 class="abs" style="left:172px;top:4118px;font-size:29px;font-weight:600;line-height:46px;color:var(--ink)">Tell us about your<br>Financial Plans.</h2>
<div class="form-label" style="left:176px;top:4226px">Firts Name</div>
<div class="form-label" style="left:415px;top:4226px">Last Name</div>
<div class="field" style="left:172px;top:4246px;width:231px;height:38px">Jhone</div>
<div class="field" style="left:413px;top:4246px;width:231px;height:38px">Due</div>
<div class="form-label" style="left:176px;top:4316px">Email</div>
<div class="form-label" style="left:415px;top:4316px">Phone</div>
<div class="field" style="left:172px;top:4337px;width:231px;height:37px">info@mailbox.example</div>
<div class="field" style="left:413px;top:4337px;width:231px;height:37px">+1 555 010 4432</div>
<div class="form-label" style="left:176px;top:4403px">Message</div>
<div class="field" style="left:172px;top:4424px;width:472px;height:103px;align-items:flex-start;padding-top:14px">I am . .</div>
<div class="btn" style="left:176px;top:4552px;width:209px;height:40px">Submit</div>
<div class="photo-back" style="left:690px;top:4160px;width:350px;height:400px"></div>
<div class="photo" role="img" aria-label="A smiling couple looking at a tablet together" style="left:671px;top:4138px;width:357px;height:406px;background:linear-gradient(135deg,#e8e4df,#c9b29a 50%,#6b7a8f)"></div>
</section>

<!-- FOOTER -->
<footer>
<div class="logo" style="left:174px;top:4700px;color:#0677BA;font-size:16px;line-height:20px"><div class="mark" style="width:44px;height:44px;background:#0677BA"></div><div>Harborline Estate<br>Partners, LLC</div></div>
<p class="abs" style="left:174px;top:4780px;width:240px;font-size:12.5px;line-height:18px;color:#2a2f3d">Stay always in touch! Subscribe to our newsletter.</p>
<div class="abs" style="left:174px;top:4828px;width:312px;height:36px;border:1px solid #9fc4e4;border-radius:18px;background:#fff;font-size:11px;color:#999;display:flex;align-items:center;padding-left:18px">Enter Your Email</div>
<svg class="abs" style="left:452px;top:4832px" width="28" height="28" viewBox="0 0 28 28"><circle cx="14" cy="14" r="14" fill="#1e9be9"/><path d="M7 14L20 8L17 21L13 16Z" fill="#fff"/></svg>
<div class="social" style="left:175px"></div>
<div class="social" style="left:231px"></div>
<div class="social" style="left:288px"></div>

<div class="abs foot-head" style="left:572px;top:4697px">Quick Links</div>
<div class="foot-link" style="top:4754px">Home</div>
<div class="foot-link" style="top:4792px">About Us</div>
<div class="foot-link" style="top:4829px">Services</div>
<div class="foot-link" style="top:4869px">FAQ</div>
<div class="foot-link" style="top:4906px">Contact Us</div>

<div class="abs foot-head" style="left:796px;top:4697px">Contact Info</div>
<div class="ci" style="top:4760px"><div class="dot"><svg width="16" height="16" viewBox="0 0 16 16"><path d="M8 1a5 5 0 0 1 5 5c0 4-5 9-5 9S3 10 3 6a5 5 0 0 1 5-5z" fill="#fff"/><circle cx="8" cy="6" r="2" fill="#1e9be9"/></svg></div><div>1840 Larkspur Lane,<br>Fenwick, Ohio</div></div>
<div class="ci" style="top:4822px"><div class="dot"><svg width="16" height="16" viewBox="0 0 16 16"><path d="M3 2h3l1 4-2 1a8 8 0 0 0 4 4l1-2 4 1v3c0 1-1 1-1 1C7 14 2 9 2 3c0 0 0-1 1-1z" fill="#fff"/></svg></div><div>(555) 014-2290</div></div>
<div class="ci" style="top:4885px"><div class="dot"><svg width="16" height="16" viewBox="0 0 16 16"><rect x="2" y="4" width="12" height="9" fill="#fff"/><path d="M2 4l6 5 6-5" fill="none" stroke="#1e9be9" stroke-width="1.3"/></svg></div><div>hello@harborlineestate.example</div></div>

<div class="abs copy">© 2022 <span>Harborline Estate Partners, LLC.</span> All rights reserved.</div>
</footer>

</body>
</html>
```